Business Cards used to invite people to our church

We are a church and have need of a business card sized advertisement that allows our members to hand them out in order to invite people to the church. I need the front of the card to say "You're Invited" or "Come Check us out". with the service times on the back of the card later.
I have attached one of the OLD cards we have used in the past, but we want a complete makeover, into a more modern style that does not require the image.
I am also replacing the old logo with a newer "flat" logo which is attached.
Please use marketing colors. (blue or red or something that catches attention)
Create a card that DOES NOT have the picture of the two people on the front
The information on the sample card back is correct to go onto new card
Target Market(s)
anyone
Industry/Entity Type
Business
Contact Information for Business Card
sertice times and address information which you can get from the sample card I uploaded. It should have "You're Invited" or "Come Check us out" on the front of the card with out logo.

```html
<!DOCTYPE html>
<html lang="en">
<head>
<meta charset="utf-8">
<title>GraceHarbor Invitation Card</title>
<link href="https://fonts.googleapis.com/css2?family=Montserrat:wght@400;500;600&family=Lobster&display=swap" rel="stylesheet">
<style>
  :root {
    --backdrop: #2f241d;
    --card-blue: #7b9bbb;
    --card-blue-light: #8eabc8;
    --card-blue-dark: #6d8db0;
    --paper: #ffffff;
    --ink: #1c1c1c;
    --leader: #555555;
  }
  * { margin: 0; padding: 0; box-sizing: border-box; }
  html, body {
    width: 1200px; height: 905px; overflow: hidden;
    background: var(--backdrop);
    font-family: "Montserrat", sans-serif;
  }
  .stage {
    position: relative; width: 1200px; height: 905px;
    display: flex; align-items: center; justify-content: center; gap: 40px;
  }
  .card {
    width: 540px; height: 309px; position: relative; overflow: hidden;
    box-shadow: 0 14px 30px rgba(0,0,0,.45);
  }

  /* Back: details side */
  .card-back { background: var(--paper); }
  .card-back .top-band {
    position: absolute; left: 0; top: 0; width: 100%; height: 82px;
    background: var(--card-blue);
    display: flex; align-items: center; justify-content: center;
  }
  .brand-name {
    color: var(--paper); font-weight: 500; font-size: 26px; letter-spacing: 1px;
  }
  .card-back .bottom-band {
    position: absolute; left: 0; bottom: 0; width: 100%; height: 26px;
    background: var(--card-blue);
  }
  .contact {
    position: absolute; top: 100px; width: 100%; text-align: center;
    color: var(--ink); font-size: 14px; font-weight: 500; line-height: 1.45;
  }
  .schedule {
    position: absolute; top: 170px; left: 70px; right: 70px;
    list-style: none; color: var(--ink); font-size: 17px; font-weight: 500;
    line-height: 1.45;
  }
  .schedule li { display: flex; align-items: baseline; }
  .schedule .leader {
    flex: 1; border-bottom: 2px dotted var(--leader); margin: 0 6px; transform: translateY(-4px);
  }

  /* Front: invitation side */
  .card-front {
    background: radial-gradient(ellipse at 30% 40%, var(--card-blue-light) 0%, var(--card-blue) 55%, var(--card-blue-dark) 100%);
  }
  .front-mark {
    position: absolute; top: 78px; width: 100%;
    display: flex; align-items: center; justify-content: center; gap: 12px;
  }
  .front-mark .dot {
    width: 26px; height: 26px; border-radius: 50%; background: var(--paper);
  }
  .front-mark .brand-name { font-size: 38px; font-weight: 600; }
  .invite-line {
    position: absolute; top: 160px; width: 100%; text-align: center;
    font-family: "Lobster", cursive; color: var(--paper); font-size: 50px;
  }
</style>
</head>
<body>
<main class="stage">
  <section class="card card-back" aria-label="Card back with service details">
    <div class="top-band"><span class="brand-name">GRACEHARBOR.org</span></div>
    <p class="contact">2480 W.Alder Lane - Brookfield, Tx 75123<br>1-800-555-0142</p>
    <ul class="schedule">
      <li><span>Sunday</span><span class="leader"></span><span>9:00 Am</span></li>
      <li><span>Sunday</span><span class="leader"></span><span>11:00 Am</span></li>
      <li><span>Wed. Bible Class</span><span class="leader"></span><span>7:00 Pm</span></li>
    </ul>
    <div class="bottom-band"></div>
  </section>

  <section class="card card-front" aria-label="Card front invitation">
    <div class="front-mark"><span class="dot"></span><span class="brand-name">GraceHarbor</span></div>
    <p class="invite-line">You're Invited</p>
  </section>
</main>
</body>
</html>
```